Renew plant-based protein powder label

I would like a redesign for my current protein powder label . The current label idea should not be altered too much, but the design should be taken to the next level. Keep in mind that is should remain professional, not too extravagant. The main color for this label should remain red, because I represent each of my products with a specific color. It would be nice if a subtle (green) touch could be implemented to represent the plant based protein.

The logo should not be altered, and I prefer designs in Adobe Indesign (so I can adjust minor things if necessary later on).
Updates

Some adjustments to my project description: I generally like the idea of my current label but think that it can be uplifted even more. For instance, I like the idea of the hexagon structures as it is now, but it can be done better (try to create a 'wow-effect'). This does not mean that I exclude any other ideas, but they should be really good as otherwise it does not make any sense switching my entire product line to the new label format. The leaf picture that I included is not mandatory to use (as I have seen this a lot). I think the way in which Design #51394062 presented the bottom information (nr. of doses etc.) is creative. But as I mentioned, I intend to adjust the whole product line to this format so it has to be really good. Thanks a lot for your efforts and I look forward to new creativity.

Target Market(s)

Fitness market. usual customer is aged 18-25.

Industry/Entity Type

Fitness. Weight lifting.

Other font styles liked:
• See fonts attached that I use now. Use no script fonts.

Colors
00AB8E
00BBA5
67D7C9
C6EFE9
E9F9F6
EB3D1F
EC4F4E
F09395
F8D3D4
FCEDEE

Requirements
Must have
• The current design idea implemented.
Nice to have
• A subtle, but creative element of the plant-based aspect. Try to keep the main color red.
Should not have
• Extravagant designs

```html
<!DOCTYPE html>
<html lang="en">
<head>
<meta charset="utf-8">
<title>Stalwart Nutrition – Label Series</title>
<link href="https://fonts.googleapis.com/css2?family=Jost:ital,wght@1,800;1,900&family=Oswald:wght@500&family=Roboto:wght@400;700;900&family=Roboto+Condensed:wght@400;700&display=swap" rel="stylesheet">
<style>
  :root{
    --page:#ffffff;
    --label-bg:#19191a;
    --ink:#ffffff;
    --ink-dark:#111111;
    --cacao:#d63b2e;
    --glow-cacao:rgba(214,30,30,.55);
    --vitamin:#fdd334;
    --glow-vitamin:rgba(230,170,20,.5);
    --plant:#1fa64a;
    --glow-plant:rgba(40,190,70,.45);
    --brand-dot:#2a7fd0;
  }
  *{box-sizing:border-box;margin:0;padding:0}
  html,body{width:1200px;height:827px;overflow:hidden;background:var(--page)}
  body{position:relative;font-family:"Roboto",Arial,sans-serif;color:var(--ink)}

  .label{
    position:absolute;left:56px;width:1087px;height:360px;overflow:hidden;
    background:var(--label-bg);
  }
  .label--cacao{top:47px}
  .label--vitamin{top:427px}

  .label__pattern{position:absolute;inset:0}
  .label--cacao .label__pattern{
    background:
      radial-gradient(ellipse 260px 260px at 130px 250px,var(--glow-cacao),transparent 70%),
      radial-gradient(ellipse 300px 260px at 950px 120px,var(--glow-plant),transparent 70%),
      linear-gradient(90deg,#221314 0%,#1a1a1b 45%,#141c16 100%);
  }
  .label--vitamin .label__pattern{
    background:
      radial-gradient(ellipse 260px 260px at 130px 230px,var(--glow-vitamin),transparent 70%),
      radial-gradient(ellipse 300px 260px at 950px 120px,var(--glow-plant),transparent 70%),
      linear-gradient(90deg,#221d12 0%,#1a1a1b 45%,#141c16 100%);
  }

  /* left column */
  .usage{position:absolute;left:35px;top:42px;width:235px;font-size:12.2px;line-height:13.3px;text-align:justify}
  .usage p{margin-bottom:13px}
  .usage b{font-weight:700}
  .usage .warning{font-size:8.8px;line-height:10.4px;font-weight:900;text-align:left;margin-top:-4px}
  .fda{
    position:absolute;left:35px;top:288px;width:233px;height:36px;
    background:#fff;color:var(--ink-dark);font-size:7.6px;line-height:9.4px;
    padding:3px 4px 0 4px;text-align:justify;
  }
  .fda span{display:block;padding-left:5px}

  /* centre */
  .brand{
    position:absolute;left:443px;top:60px;width:200px;text-align:center;
    font-family:"Roboto",Arial,sans-serif;font-weight:400;font-size:20px;letter-spacing:1.5px;line-height:22px;
  }
  .brand__dot{display:inline-block;width:10px;height:10px;border-radius:50%;background:var(--brand-dot);margin-bottom:6px}
  .product{position:absolute;left:343px;width:400px;text-align:center;font-family:"Jost",sans-serif;font-style:italic}
  .product__name{top:131px;font-size:52px;font-weight:900;letter-spacing:1px;line-height:52px}
  .label--cacao .product__name{color:var(--cacao)}
  .label--vitamin .product__name{color:var(--vitamin)}
  .product__type{top:183px;font-size:30px;font-weight:800;letter-spacing:1.2px;line-height:32px;color:var(--ink)}
  .tagline{position:absolute;left:393px;top:239px;width:300px;text-align:center;font-size:12.6px;line-height:16.5px;letter-spacing:.2px}
  .meta{position:absolute;top:298px;font-family:"Oswald",sans-serif;font-weight:500;font-size:20px;line-height:22px;transform:scaleX(.85);transform-origin:left}
  .meta--weight{left:411px}
  .meta--servings{left:604px}
  .leaf{
    position:absolute;left:688px;top:211px;width:50px;height:72px;
    background:linear-gradient(160deg,#25b24f,#138a3a);
    border-radius:50px 4px 50px 4px;
  }

  /* supplement facts */
  .facts{
    position:absolute;left:840px;top:50px;width:217px;height:204px;
    background:#fff;color:var(--ink-dark);padding:2px 5px 0 5px;
    font-family:"Roboto Condensed",Arial,sans-serif;
  }
  .facts__title{font-family:"Roboto",sans-serif;font-weight:900;font-size:15px;text-align:center;letter-spacing:.8px;line-height:17px}
  .facts__serving{font-size:8.4px;font-weight:700;line-height:8.5px;padding-left:1px}
  .facts__bar{height:4px;background:var(--ink-dark);margin:2px 0 1px}
  .facts__head{display:flex;justify-content:flex-end;font-size:8.4px;font-weight:700;line-height:10px;border-bottom:1.4px solid var(--ink-dark)}
  .facts__head span:first-child{margin-right:18px}
  .facts__row{display:flex;font-size:7.8px;line-height:9.2px;border-bottom:.6px solid #777;padding:2px 0 1px}
  .facts__row:last-of-type{border-bottom:3px solid var(--ink-dark)}
  .facts__name{flex:0 0 137px}
  .facts__amt{flex:0 0 60px}
  .facts__dv{flex:1;text-align:right}
  .facts__note{font-size:8px;line-height:10px;padding:2px 0 2px 2px;border-bottom:.8px solid var(--ink-dark)}
  .facts__other{font-size:8px;line-height:9.4px;padding:3px 0 0 2px}
  .facts__other b{font-weight:700}

  .maker{position:absolute;left:842px;top:268px;font-family:"Roboto Condensed",sans-serif;font-size:9.3px;line-height:11px}
  .maker__label{font-family:"Roboto",sans-serif;font-size:11px;margin-bottom:5px}
  .maker__name{font-weight:700}
</style>
</head>
<body>

<section class="label label--cacao">
  <div class="label__pattern" role="img" aria-label="Glowing hexagon grid background, red on the left fading to green on the right"></div>
  <div class="usage">
    <p><b>Suggested Use:</b> 1 capsule taken 1 to 2 times daily preferably with meals or as directed by a healthcare professional.</p>
    <p><b>Caution:</b> Do not exceed recommended dode. This product is not intended for pregnant or nursing mothers or children under the age of 18. If you have a known medical condition or are taking any prescription medication, consult a physician before using this or any dietary supplement. This product is manufact-tured and packaged in a facility which may also process milk, soy, wheat, egg, peanuts, tree nuts, fish and crustacean shellfish.</p>
    <p class="warning">KEEP OUT OF REACH OF CHILDREN. DO NOT USE IF SAFETY SEAL IS DAMAGED OR MISSING. STORE IN A COOL, DRY PLACE.</p>
  </div>
  <div class="fda"><span>These statements have not been evaluated by the FDA.</span>This product is not intended to diagnose, cure, treat or prevent any disease.</div>

  <div class="brand"><span class="brand__dot"></span><br>STALWART<br>NUTRITION</div>
  <h1 class="product product__name">PURE CACAO</h1>
  <h2 class="product product__type">PLANT PROTEIN</h2>
  <p class="tagline">De lekkerste én meest natuurlijke Whey.<br>Gezoet met rauw cacaopoeder.</p>
  <div class="leaf" role="img" aria-label="Green leaf illustration"></div>
  <div class="meta meta--weight">1000 G</div>
  <div class="meta meta--servings">33 SERVINGS</div>

  <div class="facts">
    <div class="facts__title">Supplement Facts</div>
    <div class="facts__serving">Serving Size:&nbsp; 1 Capsule<br>Servings Per Container: 60</div>
    <div class="facts__bar"></div>
    <div class="facts__head"><span>Amount Per Serving</span><span>%DV</span></div>
    <div class="facts__row"><span class="facts__name">Lion’s Mane 4:1 Extract<br>(Hericium erinaceus) (fruiting body)</span><span class="facts__amt">500 mg</span><span class="facts__dv">*</span></div>
    <div class="facts__row"><span class="facts__name">Chaga Mushroom 4:1 Extract<br>(fruiting body)</span><span class="facts__amt">&nbsp;50 mg</span><span class="facts__dv">*</span></div>
    <div class="facts__row"><span class="facts__name">Maitake Mushroom 4:1 Extract<br>(fruiting body)</span><span class="facts__amt">&nbsp;50 mg</span><span class="facts__dv">*</span></div>
    <div class="facts__row"><span class="facts__name">Shiitake Mushroom 4:1 Extract<br>(fruiting body)</span><span class="facts__amt">&nbsp;50 mg</span><span class="facts__dv">*</span></div>
    <div class="facts__row"><span class="facts__name">Reishi Mushroom 30% Extract<br>(fruiting body)</span><span class="facts__amt">&nbsp;50 mg</span><span class="facts__dv">*</span></div>
    <div class="facts__note">* (%DV) Daily Value not established</div>
    <div class="facts__other"><b>Other Ingredients:</b> Hydroxypropyl methylcellulosa, vegetable magnesium stearate, and silicon dioxide.</div>
  </div>
  <div class="maker">
    <div class="maker__label">Manufactured For:</div>
    <div class="maker__name">Stalwart Nutrition</div>
    418 Meadow Lane No.207<br>Fairview OH 44102
  </div>
</section>

<section class="label label--vitamin">
  <div class="label__pattern" role="img" aria-label="Glowing hexagon grid background, gold on the left fading to green on the right"></div>
  <div class="usage">
    <p><b>Suggested Use:</b> 1 capsule taken 1 to 2 times daily preferably with meals or as directed by a healthcare professional.</p>
    <p><b>Caution:</b> Do not exceed recommended dode. This product is not intended for pregnant or nursing mothers or children under the age of 18. If you have a known medical condition or are taking any prescription medication, consult a physician before using this or any dietary supplement. This product is manufact-tured and packaged in a facility which may also process milk, soy, wheat, egg, peanuts, tree nuts, fish and crustacean shellfish.</p>
    <p class="warning">KEEP OUT OF REACH OF CHILDREN. DO NOT USE IF SAFETY SEAL IS DAMAGED OR MISSING. STORE IN A COOL, DRY PLACE.</p>
  </div>
  <div class="fda"><span>These statements have not been evaluated by the FDA.</span>This product is not intended to diagnose, cure, treat or prevent any disease.</div>

  <div class="brand"><span class="brand__dot"></span><br>STALWART<br>NUTRITION</div>
  <h1 class="product product__name">VITAMINE C</h1>
  <h2 class="product product__type">ROZENBOTTEL</h2>
  <p class="tagline">De lekkerste én meest natuurlijke Whey.<br>Gezoet met rauw cacaopoeder.</p>
  <div class="leaf" role="img" aria-label="Green leaf illustration"></div>
  <div class="meta meta--weight">1000 G</div>
  <div class="meta meta--servings">33 SERVINGS</div>

  <div class="facts">
    <div class="facts__title">Supplement Facts</div>
    <div class="facts__serving">Serving Size:&nbsp; 1 Capsule<br>Servings Per Container: 60</div>
    <div class="facts__bar"></div>
    <div class="facts__head"><span>Amount Per Serving</span><span>%DV</span></div>
    <div class="facts__row"><span class="facts__name">Lion’s Mane 4:1 Extract<br>(Hericium erinaceus) (fruiting body)</span><span class="facts__amt">500 mg</span><span class="facts__dv">*</span></div>
    <div class="facts__row"><span class="facts__name">Chaga Mushroom 4:1 Extract<br>(fruiting body)</span><span class="facts__amt">&nbsp;50 mg</span><span class="facts__dv">*</span></div>
    <div class="facts__row"><span class="facts__name">Maitake Mushroom 4:1 Extract<br>(fruiting body)</span><span class="facts__amt">&nbsp;50 mg</span><span class="facts__dv">*</span></div>
    <div class="facts__row"><span class="facts__name">Shiitake Mushroom 4:1 Extract<br>(fruiting body)</span><span class="facts__amt">&nbsp;50 mg</span><span class="facts__dv">*</span></div>
    <div class="facts__row"><span class="facts__name">Reishi Mushroom 30% Extract<br>(fruiting body)</span><span class="facts__amt">&nbsp;50 mg</span><span class="facts__dv">*</span></div>
    <div class="facts__note">* (%DV) Daily Value not established</div>
    <div class="facts__other"><b>Other Ingredients:</b> Hydroxypropyl methylcellulosa, vegetable magnesium stearate, and silicon dioxide.</div>
  </div>
  <div class="maker">
    <div class="maker__label">Manufactured For:</div>
    <div class="maker__name">Stalwart Nutrition</div>
    418 Meadow Lane No.207<br>Fairview OH 44102
  </div>
</section>

</body>
</html>
```